Cover art for Zombie apocalypse book 1st in a series. I will need front, back and spine in various formats and DPIs
I am open to any idea that generally goes with the genre
I would like it eye catching and but dark
Just an FYI the full title is
The Hollowing
The Grey Dominion: Volume 1
And I will neen my name on the cover as well: Colin Ashwade

SO far the blurb is as follows:

Money, terrorism, and simple bad luck conspire to bring mankind to its knees as a viral infection spreads out of control, reducing those infected to undead horrors that feed upon the rest.

It's a time of misery and death for most, however there are some who are lucky, some who are fast, and some who are just too damned tough to go down without a fight. This is their story.

Requirements
Should not have
• The art work cannot be something that was stolen or borrowed from the internet. Do not try to give me something you don't have the rights to.

```html
<!DOCTYPE html>
<html lang="en">
<head>
<meta charset="utf-8">
<title>The Hollowing – The Grey Dominion: Volume 1 – Full Cover</title>
<link rel="stylesheet" href="https://fonts.googleapis.com/css2?family=Creepster&family=Black+Ops+One&family=Oswald:wght@500;700&display=swap">
<style>
  :root {
    --ink: #000000;
    --blood: #c8200c;
    --blood-deep: #6a0a04;
    --ember: #e38a1c;
    --ember-deep: #9a4a0a;
    --khaki: #6d6430;
    --smoke-yellow: #c9c31a;
    --smoke-green: #2f7a1a;
    --smoke-blue: #1e2f6a;
    --pale: #fff2f2;
    --pink: #f05a6e;
    --plate: #a8300f;
    --plate-dark: #7d1e08;
    --plate-text: #1a0a04;
    --web-white: #f4f0e8;
    --web-yellow: #f4e21a;
  }
  * { margin: 0; padding: 0; box-sizing: border-box; }
  html, body { width: 1200px; height: 900px; overflow: hidden; background: var(--ink); }
  .cover { position: relative; width: 1200px; height: 900px; background: var(--ink); overflow: hidden; }

  .smoke { position: absolute; }
  .smoke--back {
    left: 0; top: 120px; width: 500px; height: 620px;
    background:
      radial-gradient(ellipse 150px 110px at 270px 390px, rgba(201,195,26,.75), transparent 75%),
      radial-gradient(ellipse 220px 200px at 250px 320px, rgba(47,122,26,.55), transparent 75%),
      radial-gradient(ellipse 260px 120px at 280px 80px, rgba(30,47,106,.25), transparent 80%);
  }
  .smoke--front {
    left: 615px; top: 0; width: 585px; height: 900px;
    background:
      radial-gradient(ellipse 200px 170px at 170px 420px, rgba(201,195,26,.8), transparent 75%),
      radial-gradient(ellipse 260px 200px at 300px 330px, rgba(47,122,26,.6), transparent 78%),
      radial-gradient(ellipse 150px 120px at 300px 60px, rgba(30,47,106,.45), transparent 80%),
      radial-gradient(ellipse 200px 150px at 330px 560px, rgba(160,150,20,.35), transparent 80%);
  }
  .horde {
    position: absolute; left: 0; top: 28px; width: 490px; height: 105px;
    background:
      radial-gradient(ellipse 260px 40px at 240px 10px, rgba(201,195,26,.35), transparent 80%),
      linear-gradient(180deg, #060606 0%, #000 100%);
    border-radius: 40px 40px 0 0;
  }
  .reaching-hand {
    position: absolute; left: 825px; top: 285px; width: 150px; height: 430px;
    background: linear-gradient(180deg, #050505 0%, #000 100%);
    border-radius: 60px 60px 20px 20px;
  }

  /* Back cover */
  .blurb {
    position: absolute; left: 48px; width: 423px;
    font-family: "Black Ops One", sans-serif; font-size: 12.5px; line-height: 30px;
    letter-spacing: 1.2px; word-spacing: 4px; color: var(--blood);
    text-transform: uppercase; text-align: justify; text-align-last: center;
    -webkit-text-stroke: .4px var(--blood-deep);
  }
  .blurb--one { top: 168px; }
  .blurb--two { top: 407px; }
  .divider { position: absolute; left: 50px; top: 340px; width: 430px; height: 50px; }
  .tagline {
    position: absolute; left: 0; width: 510px; top: 590px;
    font-family: "Black Ops One", sans-serif; font-size: 17px; line-height: 39px;
    color: var(--khaki); text-align: center; text-transform: uppercase; letter-spacing: .5px;
  }
  .imprint {
    position: absolute; left: 25px; top: 683px; width: 457px; height: 192px;
    background: radial-gradient(ellipse at 60% 40%, var(--plate), var(--plate-dark));
    font-family: "Oswald", sans-serif; font-weight: 700; text-transform: uppercase;
    color: var(--plate-text);
  }
  .imprint__line { position: absolute; left: 10px; font-size: 17px; letter-spacing: .6px; line-height: 1; }
  .imprint__line--small { font-size: 12px; font-weight: 500; }
  .imprint__web { position: absolute; left: 10px; font-size: 18px; letter-spacing: .5px; color: var(--web-white); line-height: 1; }
  .imprint__web--alt { color: var(--web-yellow); }
  .imprint__price { position: absolute; left: 290px; top: 14px; font-size: 27px; letter-spacing: 1px; line-height: 1; }
  .imprint__price--gbp { left: 341px; top: 52px; font-size: 17px; font-weight: 500; }
  .imprint__code-slot { position: absolute; left: 287px; top: 85px; width: 158px; height: 97px; background: #fff; }

  /* Spine */
  .spine-series { position: absolute; left: 505px; top: 4px; width: 108px; height: 70px; }
  .spine-title { position: absolute; left: 515px; top: 118px; width: 90px; height: 470px; }
  .spine-author { position: absolute; left: 545px; top: 583px; width: 40px; height: 245px; }
  .spine-mark { position: absolute; left: 555px; top: 838px; width: 20px; height: 20px; border-radius: 50%; background: var(--blood); }
  .spine-volume {
    position: absolute; left: 505px; top: 861px; width: 120px; text-align: center;
    font-family: "Oswald", sans-serif; font-weight: 500; font-size: 15px; letter-spacing: 1px; color: var(--blood);
  }

  /* Front cover */
  .front-series { position: absolute; left: 640px; top: 25px; width: 560px; height: 240px; }
  .front-title { position: absolute; left: 630px; top: 525px; width: 570px; height: 285px; }
  .front-author { position: absolute; left: 780px; top: 842px; width: 280px; height: 50px; }

  svg text.horror { font-family: "Creepster", cursive; }
  svg text.stencil { font-family: "Black Ops One", sans-serif; }
  svg text.plain { font-family: "Oswald", sans-serif; font-weight: 500; }
</style>
</head>
<body>
<main class="cover">

  <div class="smoke smoke--back" role="img" aria-label="Swirling green and yellow toxic smoke"></div>
  <div class="smoke smoke--front" role="img" aria-label="Swirling green, yellow and blue toxic smoke"></div>
  <div class="horde" role="img" aria-label="Silhouetted crowd of the undead with glowing eyes"></div>
  <div class="reaching-hand" role="img" aria-label="Black silhouette of an undead arm reaching up from the ground"></div>

  <!-- Back cover -->
  <p class="blurb blurb--one">Money, terrorism, and simple bad luck conspire to bring mankind to its knees as a viral infection spreads out of control, reducing those infected to undead horrors that feed upon the rest.</p>

  <svg class="divider" viewBox="0 0 430 50" aria-hidden="true">
    <polygon points="5,28 190,20 195,24 185,36" fill="#a8140a"/>
    <polygon points="240,15 428,20 250,23 235,22" fill="#a8140a"/>
    <circle cx="220" cy="25" r="17" fill="#c8200c"/>
  </svg>

  <p class="blurb blurb--two">It's a time of misery and death for most, however there are some who are lucky, some who are fast, and some who are just too damned tough to go down without a fight. This is their story.</p>

  <p class="tagline">The first in a series of truely gripping<br>post apocalyptic survival epics</p>

  <section class="imprint">
    <span class="imprint__line" style="top:13px">Published 2014</span>
    <span class="imprint__line" style="top:38px">Published by ********</span>
    <span class="imprint__line" style="top:63px">Written by Colin Ashwade</span>
    <span class="imprint__line imprint__line--small" style="top:92px">Cover art by Rhea Stanmoor</span>
    <span class="imprint__web" style="top:120px">www.greydominionbook.com</span>
    <span class="imprint__web imprint__web--alt" style="top:156px">www.colinashwade.com</span>
    <span class="imprint__price">$0.00 RRP</span>
    <span class="imprint__price imprint__price--gbp">£0.00 RRP</span>
    <span class="imprint__code-slot"></span>
  </section>

  <!-- Spine -->
  <svg class="spine-series" viewBox="0 0 108 70">
    <defs>
      <linearGradient id="spinePale" x1="0" y1="0" x2="0" y2="1">
        <stop offset="0" stop-color="#ffffff"/><stop offset="1" stop-color="#f05a6e"/>
      </linearGradient>
    </defs>
    <text class="horror" x="54" y="20" text-anchor="middle" font-size="18" fill="#c8200c">THE</text>
    <text class="horror" x="54" y="62" text-anchor="middle" font-size="30" textLength="96" lengthAdjust="spacingAndGlyphs" fill="url(#spinePale)" stroke="#c8200c" stroke-width="1">HOLLOWING</text>
  </svg>

  <svg class="spine-title" viewBox="0 0 90 470">
    <defs>
      <linearGradient id="spineFire" x1="0" y1="0" x2="1" y2="0">
        <stop offset="0" stop-color="#f0a020"/><stop offset="1" stop-color="#c8200c"/>
      </linearGradient>
    </defs>
    <g transform="translate(8,0) rotate(90)">
      <text class="horror" x="5" y="-16" font-size="26" fill="#c8200c">THE</text>
      <text class="horror" x="62" y="-8" font-size="64" textLength="400" lengthAdjust="spacingAndGlyphs" fill="url(#spineFire)" stroke="#5a0804" stroke-width="1">GREY DOMINION</text>
    </g>
  </svg>

  <svg class="spine-author" viewBox="0 0 40 245">
    <defs>
      <linearGradient id="spineEmber" x1="0" y1="0" x2="1" y2="0">
        <stop offset="0" stop-color="#f0b040"/><stop offset="1" stop-color="#a05010"/>
      </linearGradient>
    </defs>
    <g transform="translate(6,0) rotate(90)">
      <text class="stencil" x="0" y="-4" font-size="24" textLength="240" lengthAdjust="spacingAndGlyphs" fill="url(#spineEmber)">COLIN ASHWADE</text>
    </g>
  </svg>

  <span class="spine-mark" aria-hidden="true"></span>
  <p class="spine-volume">VOLUME 1</p>

  <!-- Front cover -->
  <svg class="front-series" viewBox="0 0 560 240">
    <defs>
      <linearGradient id="frontPale" x1="0" y1="0" x2="0" y2="1">
        <stop offset="0" stop-color="#fff8f8"/><stop offset=".55" stop-color="#ffd8dc"/><stop offset="1" stop-color="#f05a6e"/>
      </linearGradient>
    </defs>
    <text class="horror" x="40" y="32" font-size="32" fill="#d0200c">THE</text>
    <text class="horror" x="15" y="208" font-size="190" textLength="530" lengthAdjust="spacingAndGlyphs" fill="url(#frontPale)" stroke="#c8200c" stroke-width="3">HOLLOWING</text>
    <text class="plain" x="430" y="234" font-size="28" fill="#c8200c">VOLUME 1</text>
  </svg>

  <svg class="front-title" viewBox="0 0 570 285">
    <defs>
      <linearGradient id="frontFire" x1="0" y1="0" x2="0" y2="1">
        <stop offset="0" stop-color="#e8300c"/><stop offset=".6" stop-color="#9a1606"/><stop offset="1" stop-color="#5a0804"/>
      </linearGradient>
    </defs>
    <text class="horror" x="105" y="38" font-size="40" fill="#a8180a" stroke="#3a0402" stroke-width="1">THE</text>
    <text class="horror" x="10" y="272" font-size="250" textLength="548" lengthAdjust="spacingAndGlyphs" fill="url(#frontFire)" stroke="#3a0402" stroke-width="2">GREY DOMINION</text>
  </svg>

  <svg class="front-author" viewBox="0 0 280 50">
    <defs>
      <linearGradient id="frontEmber" x1="0" y1="0" x2="0" y2="1">
        <stop offset="0" stop-color="#f4b848"/><stop offset="1" stop-color="#9a4a0a"/>
      </linearGradient>
    </defs>
    <text class="stencil" x="140" y="40" text-anchor="middle" font-size="34" textLength="262" lengthAdjust="spacingAndGlyphs" fill="url(#frontEmber)">COLIN ASHWADE</text>
  </svg>

</main>
</body>
</html>
```